Sticker label for natural moisturizer

I need a sticker label designed for a homemade moisturizer made from beef tallow and honey.
Must include: Logo, product name (Classic Suet & Clover Salve), ingredients (in English and Polish, can use placeholder text for initial design), brief description of product with instructions for use (in English and Polish, can use placeholder text for initial design), manufacturer name (vorelmart.com), manufacturer address (placeholder text for initial design), volume of container (60ml / 2oz)
The product is used by both males and females of all ages, so must be unisex design with broad appeal.
Dimensions: Length 15cm, Height 3cm
Style: Has to simultaneously communicate that this is a homemade product with no chemical fillers AND that it is of extremely high quality.
Brand colors:
#57665C
#FCFAF6
#FFFFFF
#000000
#B99B83
#EAE4DD
#CC8E5A

```html
<!DOCTYPE html>
<html lang="en">
<head>
<meta charset="utf-8">
<title>Classic Suet &amp; Clover Salve – Label</title>
<link href="https://fonts.googleapis.com/css2?family=Montserrat:wght@300;400;500;600;700&family=Amatic+SC:wght@700&display=swap" rel="stylesheet">
<style>
  :root{
    --backdrop:#2b2d2f;
    --label-tan:#A89482;
    --label-tan-light:#B59F8B;
    --sage:#57665C;
    --sage-text:#4F5E55;
    --cream:#FCFAF6;
    --logo-silver:#D5D8DB;
    --fine-text:#6E6258;
  }
  *{margin:0;padding:0;box-sizing:border-box}
  html,body{width:1100px;height:1200px;overflow:hidden;background:var(--backdrop)}
  .canvas{position:relative;width:1100px;height:1200px}
  .label{
    position:absolute;left:30px;top:385px;width:1040px;height:430px;
    background:linear-gradient(90deg,var(--label-tan-light),var(--label-tan));
    font-family:"Montserrat",sans-serif;overflow:hidden;
  }
  /* left panel: description & instructions */
  .panel-info{position:absolute;left:28px;top:40px;width:190px;
    font-size:11px;line-height:1.55;color:var(--fine-text)}
  .panel-info p+p{margin-top:12px}
  .panel-info .rule{height:1px;background:var(--sage);opacity:.5;margin:16px 0}
  .brand-mark{
    position:absolute;left:225px;top:215px;width:380px;
    transform:translate(-50%,-50%) rotate(-90deg);transform-origin:center;
    margin-left:40px;text-align:center;
    font-size:112px;font-weight:400;letter-spacing:-2px;line-height:1;
    color:var(--logo-silver);
  }
  /* centre panel */
  .title-block{
    position:absolute;left:320px;top:28px;width:420px;height:234px;
    background:var(--sage);color:var(--cream);padding:40px 0 0 30px;
  }
  .title-block .line-sm{font-size:40px;font-weight:600;line-height:1.15;letter-spacing:.5px}
  .title-block .line-lg{font-size:72px;font-weight:700;line-height:1.05;letter-spacing:2px}
  .claims{position:absolute;left:320px;top:285px;width:420px;height:88px;
    border-top:2px solid var(--sage-text);border-bottom:2px solid var(--sage-text);
    color:var(--sage-text)}
  .claims .leaf{position:absolute;left:48px;top:14px;width:80px;height:22px;
    background:var(--sage-text);border-radius:11px;opacity:.85}
  .claims .nature{position:absolute;left:32px;top:40px;font-family:"Amatic SC",sans-serif;
    font-size:34px;font-weight:700;letter-spacing:1px}
  .claims .no-fillers{position:absolute;right:14px;top:14px;text-align:center;
    font-size:27px;font-weight:600;line-height:1.2}
  .net-wt{position:absolute;left:340px;top:392px;font-size:24px;font-weight:500;color:var(--sage-text)}
  /* right panel */
  .panel-ingredients{position:absolute;left:780px;top:40px;width:220px;
    font-size:13px;line-height:1.7;color:var(--fine-text)}
  .panel-ingredients .rule{height:1px;background:var(--sage);opacity:.5;margin:18px 0}
  .maker{display:flex;gap:10px;align-items:flex-start}
  .maker svg{flex:none}
</style>
</head>
<body>
<div class="canvas">
  <div class="label">
    <div class="panel-info">
      <p>Rich whipped salve of grass-fed suet and raw clover honey. Warm a small amount between fingers and massage into dry skin.</p>
      <div class="rule"></div>
      <p>Bogaty balsam z łoju i miodu. Rozgrzej odrobinę w dłoniach i wmasuj w suchą skórę.</p>
    </div>

    <div class="brand-mark">vorel</div>

    <div class="title-block">
      <div class="line-sm">CLASSIC</div>
      <div class="line-sm">SUET &amp; CLOVER</div>
      <div class="line-lg">SALVE</div>
    </div>

    <div class="claims">
      <div class="leaf" role="img" aria-label="Small leaf sprig illustration"></div>
      <div class="nature">NATURE</div>
      <div class="no-fillers">NO CHEMICAL<br>FILLERS</div>
    </div>

    <div class="net-wt">NET WT 60ml / 2oz</div>

    <div class="panel-ingredients">
      <p>Ingredients: Beef Tallow (Talg), Olive Oil (Olea Europaea), Raw Honey (Miód), Frankincense Oil (Citrus Aurantium).</p>
      <div class="rule"></div>
      <div class="maker">
        <svg width="24" height="24" viewBox="0 0 24 24" fill="none" stroke="#57665C" stroke-width="1.5" aria-hidden="true">
          <circle cx="12" cy="12" r="10"/><ellipse cx="12" cy="12" rx="4.5" ry="10"/><path d="M2 12h20M4 7h16M4 17h16"/>
        </svg>
        <span>vorelmart.com</span>
      </div>
      <div class="rule"></div>
      <p>Made by vorelmart.com, 12 Sample Street, 00-000 Town</p>
    </div>
  </div>
</div>
</body>
</html>
```